PSD website for property company

Please read the brief thoroughly.

We are looking for a new website for a property group that does property acquisitions, property development and property management.
They buy, build and lease core inner city industrial assets in Sydney, Australia.
They also invest in residential developments.

Site menu
- Home page
- Property – sub menus include – Leasing ; Projects ; Investments ; Property Management
- Capital and finance
- About
- Contact

They like this website
https://www.verlo.com.au/

They want the site to be clean, modern and bold.
They like few colors, even black and white is OK to submit

They have a logo and style guide and useable images here:
http://www.kumet.net/temp/PelorisWeb2019.zip
The zip file is also attached to this project.
We have supplied some images to give you an idea, but we will also require you to provide at least 3 extra images from stock photos.
Use your imagination.

I am expecting a lot of similar designs, so be aware the photos you choose will be really important.
They want really 3 good stock photos used and supplied without charge.
Please not too generic, I repeat the quality of the photos is important.
You may provide several photos (but not in multiple submissions please) and we will choose the best three to be provided.

The winner will be selected on a single home page design and required to provide;
All photos use in original format without charge
A second ‘standard page’ template design based on the winning home page design

```html
<!DOCTYPE html>
<html lang="en">
<head>
<meta charset="utf-8">
<title>Peloris — Property Development &amp; Construction</title>
<link rel="stylesheet" href="https://fonts.googleapis.com/css2?family=Archivo+Black&family=Montserrat:wght@400;500;600;700&family=Arimo:wght@400;700&display=swap">
<style>
:root{
  --green:#5b6f2b;
  --green-dark:#4a5d1f;
  --link:#4f6a1c;
  --white:#ffffff;
  --text:#555555;
  --footer:#3d3d3d;
  --footer-dark:#2f2f2f;
}
*{box-sizing:border-box;margin:0;padding:0}
html,body{width:1200px;height:3380px;overflow:hidden;background:var(--white)}
body{position:relative;font-family:Arimo,Arial,sans-serif;color:var(--text)}
.abs{position:absolute}

/* hero */
.hero{left:0;top:0;width:1200px;height:532px;background:linear-gradient(180deg,#7f9bc4 0%,#8fa3b9 35%,#7a8b82 70%,#6a7a4e 100%)}
.logo{left:0;width:1200px;top:18px;text-align:center;font-family:Montserrat,sans-serif;font-weight:500;font-size:50px;letter-spacing:12px;color:var(--white)}
.nav-rule{left:0;top:92px;width:1200px;height:1px;background:rgba(255,255,255,.8)}
.nav{left:0;top:100px;width:1200px;display:flex;justify-content:center;align-items:center;font-family:Montserrat,sans-serif;font-weight:600;font-size:12px;color:var(--white)}
.nav span{padding:0 14px}
.nav .sep{padding:0}
.nav .cta{background:var(--green);padding:9px 8px;border-radius:2px;margin-left:12px}
.bracket{top:151px;width:68px;height:324px;border:9px solid var(--white)}
.bracket.l{left:105px;border-right:none}
.bracket.r{left:993px;border-left:none}
.tagline{left:0;width:1200px;top:170px;text-align:center;font-family:Arimo,sans-serif;font-size:31px;color:var(--white)}
.title{left:0;width:1200px;top:224px;text-align:center;font-family:"Archivo Black",sans-serif;font-size:48px;line-height:62px;letter-spacing:5px;color:var(--white)}
.btn-invest{left:520px;top:420px;width:156px;height:49px;background:var(--green);color:var(--white);font-family:Montserrat,sans-serif;font-weight:700;font-size:16px;display:flex;align-items:center;justify-content:center}
.dot{top:424px;width:18px;height:18px;border-radius:50%;border:2px solid var(--white);background:rgba(255,255,255,.25)}
.dot::after{content:"";position:absolute;left:3px;top:3px;width:8px;height:8px;border-radius:50%;background:var(--white)}
.scroll{left:586px;top:509px;width:28px;height:62px;border:2px solid var(--green);border-radius:14px;background:var(--white)}

/* stats */
.stats{left:0;top:635px;width:1200px;height:175px;background:linear-gradient(90deg,#6f8153,#7f9068 50%,#6b7d4c)}
.stat{top:675px;height:96px;border:4px solid var(--white);display:flex;align-items:center;justify-content:center;text-align:center;font-family:"Archivo Black",sans-serif;font-size:25px;line-height:31px;color:var(--white)}

/* services */
.card-img{width:287px;height:191px}
.card-img::after{content:"";position:absolute;left:40px;top:10px;right:8px;bottom:10px;border:1px solid rgba(255,255,255,.7)}
.card-label{background:var(--white);font-family:Arimo,sans-serif;font-size:21px;line-height:24px;color:var(--green-dark);text-align:center;padding:6px 8px}
.card-text{font-size:12.5px;line-height:16px;color:var(--text);width:262px}
.card-link{font-family:Arimo,sans-serif;font-size:14.5px;line-height:18px;color:var(--link)}
.go{width:40px;height:40px;border-radius:50%;background:var(--green)}

/* about */
.about-img{left:0;top:1804px;width:572px;height:556px;background:linear-gradient(180deg,#b7c8de 0%,#c9b7a5 40%,#7c8a6a 70%,#3f78b0 100%)}
.about-panel{left:572px;top:1804px;width:628px;height:615px;background:var(--green)}
.about-title{left:643px;top:1858px;font-family:Arimo,sans-serif;font-weight:400;font-size:31px;color:var(--white);border-bottom:3px solid var(--white);padding-bottom:2px}
.about-text{left:643px;top:1930px;width:411px;font-size:13px;line-height:20.3px;color:var(--white);text-align:justify}

/* form */
.form-sec{left:0;top:2537px;width:1200px;height:680px;background:linear-gradient(90deg,#62783a,#6f8446 50%,#667b3d)}
.form-title{left:357px;top:2595px;font-size:31px;font-weight:400;color:var(--white);border-bottom:3px solid var(--white);padding-bottom:1px}
.looking{left:355px;top:2695px;font-size:15px;color:var(--white)}
.chip{top:2693px;width:100px;height:29px;border:1.5px solid var(--white);border-radius:6px;color:var(--white);font-size:11px;font-weight:700;display:flex;align-items:center;justify-content:center}
.chip.on{background:var(--white);color:var(--green-dark)}
.field{left:357px;width:494px;border:1.5px solid rgba(255,255,255,.8);border-radius:3px}
.field-label{left:385px;font-family:Montserrat,sans-serif;font-weight:700;font-size:11px;color:var(--white)}
.agree{left:357px;top:3038px;display:flex;align-items:center;gap:8px;font-size:11px;color:var(--white)}
.box{width:14px;height:14px;border:1.5px solid var(--white)}
.submit{left:354px;top:3097px;width:136px;height:50px;background:var(--white);border-radius:3px;font-size:18px;color:#333;display:flex;align-items:center;justify-content:center}

/* footer */
.footer{left:0;top:3217px;width:1200px;height:118px;background:var(--footer)}
.fnav{left:0;width:1200px;top:3244px;display:flex;justify-content:center;font-family:Montserrat,sans-serif;font-weight:600;font-size:14px;color:var(--white)}
.fnav span{padding:0 12px}
.fnav .sep{padding:0}
.privacy{left:0;width:1200px;top:3283px;display:flex;justify-content:center;align-items:center;gap:8px;font-family:Montserrat,sans-serif;font-weight:600;font-size:13px;color:var(--white)}
.bottom{left:0;top:3335px;width:1200px;height:45px;background:var(--footer-dark)}
.legal{left:105px;top:3351px;font-size:11px;color:var(--white)}
.flogo{left:0;width:1200px;top:3337px;text-align:center;font-family:Montserrat,sans-serif;font-weight:500;font-size:32px;letter-spacing:8px;color:var(--white)}
.social{top:3351px;width:14px;height:14px;border-radius:3px;background:#4d5a2e}
</style>
</head>
<body>

<!-- hero -->
<div class="abs hero" role="img" aria-label="Modern arched building with a landscaped public lawn and people walking"></div>
<div class="abs logo">PELORIS</div>
<div class="abs nav-rule"></div>
<nav class="abs nav">
  <span>Home</span><span class="sep">|</span>
  <span>Property ▾</span><span class="sep">|</span>
  <span>Capital &amp; Finance</span><span class="sep">|</span>
  <span>About us</span><span class="sep">|</span>
  <span class="cta">Contact us</span>
</nav>
<div class="abs bracket l"></div>
<div class="abs bracket r"></div>
<div class="abs tagline">You Dream it we do it</div>
<h1 class="abs title">PROPERTY DEVELOPMENT &amp;<br>CONSTRUCTION</h1>
<div class="abs btn-invest">Investment</div>
<div class="abs dot" style="left:917px"></div>
<div class="abs dot" style="left:949px"></div>
<div class="abs dot" style="left:982px"></div>
<div class="abs scroll">
  <svg width="24" height="58" viewBox="0 0 24 58"><path d="M12 18v22M7 35l5 6 5-6" fill="none" stroke="#333" stroke-width="1.5"/></svg>
</div>

<!-- stats -->
<div class="abs stats" role="img" aria-label="City skyline with office towers, green tint"></div>
<div class="abs stat" style="left:105px;width:192px">500 Project<br>Delivered</div>
<div class="abs stat" style="left:330px;width:193px">15 Years<br>Experience</div>
<div class="abs stat" style="left:559px;width:260px">Best Enginneer &amp;<br>Architech Team</div>
<div class="abs stat" style="left:853px;width:207px">1500 Investor<br>Family</div>

<!-- services row 1 -->
<div class="abs card-img" style="left:98px;top:905px;background:linear-gradient(180deg,#3f7fd0,#9fb8c8 60%,#5b6a6a)" role="img" aria-label="Curved residential tower against blue sky"></div>
<div class="abs card-label" style="left:138px;top:1064px;width:210px">Development &amp;<br>Construction</div>
<div class="abs card-text" style="left:111px;top:1128px">The standard chunk of Lorem Ipsum used since the 1500s is reproduced below for those</div>
<div class="abs card-link" style="left:111px;top:1198px">Checkout our on going<br>development Project</div>
<div class="abs go" style="left:329px;top:1197px"><svg width="40" height="40"><path d="M11 20h18M25 16l4 4-4 4" fill="none" stroke="#fff" stroke-width="1.5"/></svg></div>

<div class="abs card-img" style="left:435px;top:905px;background:linear-gradient(180deg,#e6ecf0,#3c6fa8 40%,#7d8a6c)" role="img" aria-label="Hotel atrium restaurant with glass roof and plants"></div>
<div class="abs card-label" style="left:475px;top:1064px;width:210px;letter-spacing:1.5px">Hotel &amp;<br>Resturent</div>
<div class="abs card-text" style="left:446px;top:1128px">The standard chunk of Lorem Ipsum used since the 1500s is reproduced below for those</div>
<div class="abs card-link" style="left:446px;top:1203px">Visit our Hotel and Resturent</div>
<div class="abs go" style="left:689px;top:1197px"><svg width="40" height="40"><path d="M11 20h18M25 16l4 4-4 4" fill="none" stroke="#fff" stroke-width="1.5"/></svg></div>

<div class="abs card-img" style="left:771px;top:905px;background:linear-gradient(180deg,#7fa3c8,#4d7ea0 50%,#8c7a6a)" role="img" aria-label="Waterfront apartment balcony overlooking a harbour"></div>
<div class="abs card-label" style="left:811px;top:1068px;width:215px">Property Investment</div>
<div class="abs card-text" style="left:780px;top:1128px">The standard chunk of Lorem Ipsum used since the 1500s is reproduced below for those</div>
<div class="abs card-link" style="left:790px;top:1203px">Checkout Investment Projects</div>
<div class="abs go" style="left:1017px;top:1197px"><svg width="40" height="40"><path d="M11 20h18M25 16l4 4-4 4" fill="none" stroke="#fff" stroke-width="1.5"/></svg></div>

<!-- services row 2 -->
<div class="abs card-img" style="left:100px;top:1299px;background:linear-gradient(180deg,#7fb2e0,#e8ecef 45%,#3fb0d8)" role="img" aria-label="Apartment complex with a swimming pool and palm trees"></div>
<div class="abs card-label" style="left:138px;top:1459px;width:214px;text-align:left;padding-left:36px">Property<br>Management<br>&amp; Sell</div>
<div class="abs card-text" style="left:125px;top:1550px">The standard chunk of Lorem Ipsum used since the 1500s is reproduced below for those</div>
<div class="abs card-link" style="left:115px;top:1659px">Visit&nbsp; Current selling Property</div>
<div class="abs go" style="left:329px;top:1650px"><svg width="40" height="40"><path d="M11 20h18M25 16l4 4-4 4" fill="none" stroke="#fff" stroke-width="1.5"/></svg></div>

<div class="abs card-img" style="left:435px;top:1299px;background:linear-gradient(135deg,#2e5db8,#8fb0e0 50%,#1f4a9a)" role="img" aria-label="Glass office towers seen from below"></div>
<div class="abs card-label" style="left:475px;top:1459px;width:210px">Leasing &amp; Finance</div>
<div class="abs card-text" style="left:452px;top:1550px">The standard chunk of Lorem Ipsum used since the 1500s is reproduced below for those</div>
<div class="abs card-link" style="left:457px;top:1662px">Leasing hold Property</div>
<div class="abs go" style="left:689px;top:1652px"><svg width="40" height="40"><path d="M11 20h18M25 16l4 4-4 4" fill="none" stroke="#fff" stroke-width="1.5"/></svg></div>

<div class="abs card-img" style="left:769px;top:1299px;background:linear-gradient(135deg,#9cc0e6,#e9eef2 45%,#3f6a2f)" role="img" aria-label="Modern white villa with glass walls and garden"></div>
<div class="abs card-label" style="left:809px;top:1459px;width:210px">Rent &amp; Buy</div>
<div class="abs card-text" style="left:793px;top:1550px">The standard chunk of Lorem Ipsum used since the 1500s is reproduced below for those</div>
<div class="abs card-link" style="left:790px;top:1659px">Visit&nbsp; Rent Property</div>
<div class="abs go" style="left:1017px;top:1650px"><svg width="40" height="40"><path d="M11 20h18M25 16l4 4-4 4" fill="none" stroke="#fff" stroke-width="1.5"/></svg></div>

<!-- about -->
<div class="abs about-img" role="img" aria-label="Large family house with gabled roof and a pool in front at dusk"></div>
<div class="abs about-panel"></div>
<svg class="abs" style="left:530px;top:2360px" width="42" height="59"><polygon points="42,0 42,59 40,59 0,28 42,0" fill="#5b6f2b"/></svg>
<h2 class="abs about-title">About Our Journey</h2>
<p class="abs about-text">Our story began with a single warehouse on the edge of the city and a simple belief that good buildings make better neighbourhoods. Over fifteen years we have grown from a small team of builders into a full property group that acquires, develops and manages inner city industrial assets, and invests in carefully chosen residential projects. Every site we take on is studied closely, from its history and its streets to the people who will one day live and work there. We plan with care, build with trusted engineers and architects, and stay close to each project long after the keys are handed over. Our investor family has grown alongside us, sharing in steady returns and in the pride of places that last. Today we lease, sell and maintain a portfolio that spans offices, hotels, homes and logistics spaces, yet the way we work has not changed. We listen first, we keep our promises, and we measure success by the value our buildings bring to their owners, tenants and the wider community for many years to come.</p>
<svg class="abs" style="left:648px;top:2313px" width="48" height="16"><path d="M1 8h44M39 3l6 5-6 5" fill="none" stroke="#fff" stroke-width="2"/></svg>

<!-- form -->
<div class="abs form-sec" role="img" aria-label="Residential apartment blocks with a tree-lined walkway, green tint"></div>
<h2 class="abs form-title">Get Latest Update of new Projects</h2>
<div class="abs looking">I am looing for...</div>
<div class="abs chip on" style="left:475px">Latest update</div>
<div class="abs chip" style="left:590px">Investing</div>
<div class="abs chip" style="left:712px">Sell or Buy</div>
<div class="abs chip" style="left:827px">Leasing</div>
<div class="abs field-label" style="top:2747px">Name</div>
<div class="abs field" style="top:2760px;height:32px"></div>
<div class="abs field-label" style="top:2797px">Phone</div>
<div class="abs field" style="top:2802px;height:33px"></div>
<div class="abs field-label" style="top:2855px">Email</div>
<div class="abs field" style="top:2861px;height:32px"></div>
<div class="abs field-label" style="top:2912px">Message</div>
<div class="abs field" style="top:2918px;height:76px"></div>
<div class="abs agree"><span class="box"><svg width="12" height="12"><path d="M2 6l3 3 5-6" fill="none" stroke="#fff" stroke-width="1.5"/></svg></span>I agree with Term &amp; Condition</div>
<div class="abs submit">Submit</div>

<!-- footer -->
<div class="abs footer"></div>
<nav class="abs fnav">
  <span>Home</span><span class="sep">|</span>
  <span>Property</span><span class="sep">|</span>
  <span>Capital &amp; Finance</span><span class="sep">|</span>
  <span>About us</span><span class="sep">|</span>
  <span>Contact us</span>
</nav>
<div class="abs privacy">See Privacy Policy <svg width="34" height="10"><path d="M1 5h30M26 1l5 4-5 4" fill="none" stroke="#fff" stroke-width="1.5"/></svg></div>
<div class="abs bottom"></div>
<div class="abs legal">Term of Use | Privacy Policy</div>
<div class="abs flogo">PELORIS</div>
<div class="abs social" style="left:903px"></div>
<div class="abs social" style="left:939px"></div>
<div class="abs social" style="left:974px"></div>
<div class="abs social" style="left:1009px"></div>
<div class="abs social" style="left:1045px"></div>

</body>
</html>
```